Lantern Method of Ascent Programme Graphic

Please refer to attached graphic.
I wish to redesign this graphic to represent a programme of work that we (Quelvaro) deliver to our customers.
The design represents 9 steps ( 3 steps at each of 3 levels) and is all about implementing the 'Lantern Method of Ascent'

I like the fact that the increasing business growth is evident when you are progressing through the stages, but the current graphic looks dated and the colours are not working.
I would also like to incorporate the LMA logo we have created.

Target Market(s)

IT Sector - businesses looking to grow

Industry/Entity Type

We are a digital marketing company

Requirements
Must have
• Clear, concise design
Should not have
• Design must not be complicated

```html
<!DOCTYPE html>
<html lang="en">
<head>
<meta charset="utf-8">
<title>Lantern Method of Ascent Programme</title>
<link rel="stylesheet" href="https://fonts.googleapis.com/css2?family=Fira+Sans:wght@600&family=Noto+Sans:ital,wght@0,400;1,400&display=swap">
<style>
  :root {
    --bg-deep: #0b1a36;
    --bg-mid: #112a4f;
    --glow: #22628f;
    --cyan: #13b4ef;
    --cyan-soft: #2aa3da;
    --hex-fill: #13294f;
    --bar: #3158a8;
    --bar-light: #5a82c6;
    --title: #c9ecfb;
    --body: #d8eefa;
    --brand: #2aa9e2;
  }
  * { margin: 0; padding: 0; box-sizing: border-box; }
  html, body { width: 1200px; height: 675px; overflow: hidden; background: var(--bg-deep); }
  .canvas {
    position: relative;
    width: 1200px; height: 675px; overflow: hidden;
    background:
      radial-gradient(ellipse 420px 300px at 560px 440px, rgba(34,98,143,0.75), rgba(34,98,143,0) 70%),
      linear-gradient(120deg, var(--bg-mid) 0%, var(--bg-deep) 60%, #0a1833 100%);
    font-family: "Noto Sans", sans-serif;
  }
  .circuit-field {
    position: absolute; left: 0; top: 0; width: 420px; height: 675px;
    background: linear-gradient(90deg, rgba(30,90,140,0.45) 0%, rgba(20,60,110,0.25) 60%, rgba(20,60,110,0) 100%);
  }
  .artwork { position: absolute; left: 0; top: 0; }
  .hub-label {
    position: absolute; left: 184px; top: 401px; width: 182px;
    text-align: center; color: var(--title);
    font-family: "Fira Sans", sans-serif; font-weight: 600;
    font-size: 29px; line-height: 35px; letter-spacing: 0.5px;
  }
  .stage {
    position: absolute; top: 337px; width: 230px; margin-left: -115px;
    text-align: center; color: var(--body);
  }
  .stage-mark {
    font-family: "Fira Sans", sans-serif; font-weight: 600;
    font-size: 20px; line-height: 24px; color: var(--cyan-soft); letter-spacing: 2px;
  }
  .stage-title {
    margin-top: 47px;
    font-family: "Fira Sans", sans-serif; font-weight: 600;
    font-size: 31px; line-height: 36px; color: var(--title);
  }
  .stage-cadence { margin-top: 6px; font-size: 19px; line-height: 22px; letter-spacing: 0.3px; }
  .stage-focus { font-style: italic; font-size: 15.5px; line-height: 20px; letter-spacing: 0.3px; }
  .stage-steps { list-style: none; margin-top: 7px; font-size: 14.5px; line-height: 17.5px; letter-spacing: 0.3px; }
  .brand {
    position: absolute; left: 1040px; top: 606px; width: 124px; text-align: right;
    font-family: "Fira Sans", sans-serif; font-weight: 600;
    font-size: 28px; line-height: 34px; color: var(--brand);
  }
</style>
</head>
<body>
<main class="canvas">
  <div class="circuit-field" role="img" aria-label="Decorative circuit board pattern in blue tones"></div>

  <svg class="artwork" width="1200" height="675" viewBox="0 0 1200 675" aria-hidden="true">
    <defs>
      <filter id="hex-glow" x="-30%" y="-30%" width="160%" height="160%">
        <feGaussianBlur stdDeviation="6"/>
      </filter>
    </defs>

    <g class="frame-lines" fill="none" stroke="#1d4a7c" stroke-width="1" opacity="0.7">
      <polyline points="400,20 1085,20 1200,105"/>
      <polyline points="390,34 1125,34 1200,92"/>
      <polyline points="400,628 1085,628 1200,520"/>
    </g>

    <g class="growth-bars">
      <g fill="var(--bar)">
        <rect x="446" y="223.5" width="33" height="7"/><rect x="446" y="237.5" width="33" height="7"/><rect x="446" y="251.5" width="33" height="7"/>
        <rect x="489" y="223.5" width="33" height="7"/><rect x="489" y="237.5" width="33" height="7"/><rect x="489" y="251.5" width="33" height="7"/>
        <rect x="533" y="223.5" width="33" height="7"/><rect x="533" y="237.5" width="33" height="7"/><rect x="533" y="251.5" width="33" height="7"/>
        <rect x="576" y="223.5" width="33" height="7"/><rect x="576" y="237.5" width="33" height="7"/><rect x="576" y="251.5" width="33" height="7"/>
        <rect x="619" y="223.5" width="33" height="7"/><rect x="619" y="237.5" width="33" height="7"/><rect x="619" y="251.5" width="33" height="7"/>
      </g>
      <g fill="var(--bar)">
        <rect x="663" y="181" width="33" height="7"/><rect x="663" y="195" width="33" height="7"/><rect x="663" y="209" width="33" height="7"/><rect x="663" y="223.5" width="33" height="7"/><rect x="663" y="237.5" width="33" height="7"/><rect x="663" y="251.5" width="33" height="7"/>
        <rect x="706" y="181" width="33" height="7"/><rect x="706" y="195" width="33" height="7"/><rect x="706" y="209" width="33" height="7"/><rect x="706" y="223.5" width="33" height="7"/><rect x="706" y="237.5" width="33" height="7"/><rect x="706" y="251.5" width="33" height="7"/>
        <rect x="749" y="181" width="33" height="7"/><rect x="749" y="195" width="33" height="7"/><rect x="749" y="209" width="33" height="7"/><rect x="749" y="223.5" width="33" height="7"/><rect x="749" y="237.5" width="33" height="7"/><rect x="749" y="251.5" width="33" height="7"/>
        <rect x="793" y="181" width="33" height="7"/><rect x="793" y="195" width="33" height="7"/><rect x="793" y="209" width="33" height="7"/><rect x="793" y="223.5" width="33" height="7"/><rect x="793" y="237.5" width="33" height="7"/><rect x="793" y="251.5" width="33" height="7"/>
        <rect x="836" y="181" width="33" height="7"/><rect x="836" y="195" width="33" height="7"/><rect x="836" y="209" width="33" height="7"/><rect x="836" y="223.5" width="33" height="7"/><rect x="836" y="237.5" width="33" height="7"/><rect x="836" y="251.5" width="33" height="7"/>
      </g>
      <g>
        <g fill="var(--bar-light)">
          <rect x="879" y="139" width="33" height="7"/><rect x="879" y="153" width="33" height="7"/><rect x="879" y="167" width="33" height="7"/>
          <rect x="923" y="139" width="33" height="7"/><rect x="923" y="153" width="33" height="7"/><rect x="923" y="167" width="33" height="7"/>
          <rect x="966" y="139" width="33" height="7"/><rect x="966" y="153" width="33" height="7"/><rect x="966" y="167" width="33" height="7"/>
          <rect x="1009" y="139" width="33" height="7"/><rect x="1009" y="153" width="33" height="7"/><rect x="1009" y="167" width="33" height="7"/>
          <rect x="1052" y="139" width="33" height="7"/><rect x="1052" y="153" width="33" height="7"/><rect x="1052" y="167" width="33" height="7"/>
        </g>
        <g fill="var(--bar)">
          <rect x="879" y="181" width="33" height="7"/><rect x="879" y="195" width="33" height="7"/><rect x="879" y="209" width="33" height="7"/><rect x="879" y="223.5" width="33" height="7"/><rect x="879" y="237.5" width="33" height="7"/><rect x="879" y="251.5" width="33" height="7"/>
          <rect x="923" y="181" width="33" height="7"/><rect x="923" y="195" width="33" height="7"/><rect x="923" y="209" width="33" height="7"/><rect x="923" y="223.5" width="33" height="7"/><rect x="923" y="237.5" width="33" height="7"/><rect x="923" y="251.5" width="33" height="7"/>
          <rect x="966" y="181" width="33" height="7"/><rect x="966" y="195" width="33" height="7"/><rect x="966" y="209" width="33" height="7"/><rect x="966" y="223.5" width="33" height="7"/><rect x="966" y="237.5" width="33" height="7"/><rect x="966" y="251.5" width="33" height="7"/>
          <rect x="1009" y="181" width="33" height="7"/><rect x="1009" y="195" width="33" height="7"/><rect x="1009" y="209" width="33" height="7"/><rect x="1009" y="223.5" width="33" height="7"/><rect x="1009" y="237.5" width="33" height="7"/><rect x="1009" y="251.5" width="33" height="7"/>
          <rect x="1052" y="181" width="33" height="7"/><rect x="1052" y="195" width="33" height="7"/><rect x="1052" y="209" width="33" height="7"/><rect x="1052" y="223.5" width="33" height="7"/><rect x="1052" y="237.5" width="33" height="7"/><rect x="1052" y="251.5" width="33" height="7"/>
        </g>
      </g>
    </g>

    <g class="value-hub">
      <polygon points="269,252 431,345 431,531 269,624 107,531 107,345" fill="none" stroke="var(--cyan-soft)" stroke-width="1.2"/>
      <polygon points="269,275 410,356 410,519 269,601 128,519 128,356" fill="none" stroke="var(--cyan)" stroke-width="10" opacity="0.55" filter="url(#hex-glow)"/>
      <polygon points="269,275 410,356 410,519 269,601 128,519 128,356" fill="var(--hex-fill)"/>
      <polygon points="269,320 371,380 371,496 269,555 167,496 167,380" fill="#0f2347" stroke="var(--cyan-soft)" stroke-width="2"/>
      <polygon points="269,348 347,394 347,482 269,527 191,482 191,394" fill="#0c1c3b" stroke="var(--cyan-soft)" stroke-width="0.8"/>
    </g>

    <g class="connector" fill="none" stroke="var(--cyan)" stroke-width="2">
      <polyline points="269,564 378,502 376,293 984,293"/>
      <line x1="515" y1="293" x2="554" y2="317"/>
      <line x1="759" y1="293" x2="797" y2="317"/>
      <line x1="984" y1="293" x2="1022" y2="317"/>
    </g>
  </svg>

  <div class="hub-label">BUSINESS VALUE</div>

  <section class="stage" style="left:570px;">
    <div class="stage-mark">LMA</div>
    <h2 class="stage-title">Lantern</h2>
    <p class="stage-cadence">Numbers that Matter</p>
    <p class="stage-focus">Foundation Metric</p>
    <ul class="stage-steps"><li>Personas</li><li>Database</li><li>Systems</li></ul>
  </section>

  <section class="stage" style="left:798px;">
    <div class="stage-mark">LMA</div>
    <h2 class="stage-title">Method</h2>
    <p class="stage-cadence">Weekly Scorecard</p>
    <p class="stage-focus">Tactical Execution</p>
    <ul class="stage-steps"><li>Messaging</li><li>Leads</li><li>Pipeline</li></ul>
  </section>

  <section class="stage" style="left:1028px;">
    <div class="stage-mark">LMA</div>
    <h2 class="stage-title">Ascent</h2>
    <p class="stage-cadence">Monthly Scorecard</p>
    <p class="stage-focus">Strategic Review</p>
    <ul class="stage-steps"><li>Sales</li><li>Nurture</li><li>Reference</li></ul>
  </section>

  <div class="brand">Quelvaro</div>
</main>
</body>
</html>
```